Biz Card for Harrowfield Property Partners - HWPP

Harrowfield Property Partners is a commercial real estate acquisitions firm. We buy commercial property and need to raise capital from investors for each deal we buy. The vibe needs to be: give us your money, we will multiply it.
Our website: www.hrwpp-example.com
Competitors are: https://velmarholdings-example.com/, https://tribanquepartners-example.com/, http://www.ostrellecapital-example.com/
Target Market(s)
High Net Worth Individuals, Bankers, Insurance Companies, Commercial Real Estate Brokers.
Industry/Entity Type
Investment Banking
Contact Information for Business Card
Name, Title, Addess, Cell#, Office#, email, website
Requirements
Must have
- use one of our logos. See website for look and feel: www.hrwpp-example.com
Nice to have
- see website: www.hrwpp-example.com

```html
<!DOCTYPE html>
<html lang="en">
<head>
<meta charset="utf-8">
<title>Harrowfield Property Partners – Business Card</title>
<link rel="stylesheet" href="https://fonts.googleapis.com/css2?family=Lato:wght@400;700;900&display=swap">
<style>
  :root {
    --bg: #2b2b2e;
    --card-white: #ffffff;
    --navy: #0f2a44;
    --navy-deep: #0a2138;
    --slate-top: #4a4b54;
    --grey-text: #8a8a8e;
    --rule: #4d5566;
  }
  * { box-sizing: border-box; margin: 0; padding: 0; }
  html, body { width: 1200px; height: 1108px; overflow: hidden; }
  body {
    background: var(--bg);
    font-family: "Lato", sans-serif;
    position: relative;
  }
  .card {
    position: absolute;
    top: 174px;
    width: 440px;
    height: 760px;
    border-radius: 22px;
    box-shadow: 0 18px 40px rgba(0,0,0,.45);
  }
  .card--front {
    left: 120px;
    background: var(--card-white);
    display: flex;
    flex-direction: column;
    align-items: center;
    padding-top: 70px;
    text-align: center;
  }
  .card--back {
    left: 640px;
    background: linear-gradient(180deg, var(--slate-top) 0%, var(--navy-deep) 100%);
  }
  .brand-mark {
    width: 96px; height: 96px;
    border-radius: 50%;
    background: var(--navy);
  }
  .brand-name {
    margin-top: 22px;
    color: var(--navy);
    font-weight: 400;
    line-height: 1.25;
  }
  .brand-name__main { display: block; font-size: 34px; letter-spacing: 8px; }
  .brand-name__sub { display: block; font-size: 15px; letter-spacing: 5px; }
  .person-name {
    margin-top: 52px;
    font-size: 36px;
    font-weight: 900;
    color: var(--navy);
    letter-spacing: .5px;
  }
  .person-title {
    margin-top: 4px;
    font-size: 20px;
    color: var(--grey-text);
  }
  .icon-rule {
    margin-top: 24px;
    width: 330px;
    display: flex;
    align-items: center;
    gap: 10px;
  }
  .icon-rule::before, .icon-rule::after {
    content: ""; flex: 1; height: 1px; background: var(--rule);
  }
  .contact-icons { display: flex; gap: 5px; }
  .contact-list {
    margin-top: 16px;
    list-style: none;
    font-size: 21px;
    line-height: 1.45;
    color: var(--grey-text);
  }
  .rule {
    margin-top: 14px;
    width: 330px; height: 1px; background: var(--rule);
  }
  .address {
    margin-top: 14px;
    font-style: normal;
    font-size: 21px;
    line-height: 1.45;
    color: var(--grey-text);
  }
  .back-name {
    position: absolute;
    left: 0; right: 0; bottom: 110px;
    text-align: center;
    color: #ffffff;
    font-weight: 400;
    line-height: 1.3;
  }
  .back-name .brand-name__main { font-size: 34px; }
</style>
</head>
<body>
  <section class="card card--front" aria-label="Business card front">
    <div class="brand-mark" aria-hidden="true"></div>
    <p class="brand-name">
      <span class="brand-name__main">HARROWFIELD</span>
      <span class="brand-name__sub">PROPERTY PARTNERS</span>
    </p>
    <h1 class="person-name">DANIEL ORRIN</h1>
    <p class="person-title">Founder &amp; CEO</p>
    <div class="icon-rule">
      <svg class="contact-icons" width="122" height="28" viewBox="0 0 122 28" aria-hidden="true">
        <g fill="#0f2a44">
          <circle cx="14" cy="14" r="13"/><circle cx="45" cy="14" r="13"/>
          <circle cx="76" cy="14" r="13"/><circle cx="107" cy="14" r="13"/>
        </g>
        <g fill="none" stroke="#fff" stroke-width="1.6" stroke-linecap="round" stroke-linejoin="round">
          <path d="M9 8 l3 0 l1.5 4 l-2 1.5 a8 8 0 0 0 4 4 l1.5 -2 l4 1.5 l0 3 a2 2 0 0 1 -2 2 a13 13 0 0 1 -12 -12 a2 2 0 0 1 2 -2z"/>
          <rect x="40" y="6" width="10" height="16" rx="1.5"/><path d="M43.5 19.5 h3"/>
          <rect x="69" y="9" width="14" height="10" rx="1"/><path d="M69 9 l7 6 l7 -6"/>
          <circle cx="107" cy="14" r="7"/><path d="M100 14 h14 M107 7 c-4 4 -4 10 0 14 c4 -4 4 -10 0 -14"/>
        </g>
      </svg>
    </div>
    <ul class="contact-list">
      <li>111 555 0142</li>
      <li>111 555 0142</li>
      <li>info@hrwpp-example.com</li>
      <li>www.hrwpp-example.com</li>
    </ul>
    <div class="rule"></div>
    <address class="address">
      1234 First Line Address<br>
      5678 Second Line Address
    </address>
  </section>

  <section class="card card--back" aria-label="Business card back">
    <p class="back-name">
      <span class="brand-name__main">HARROWFIELD</span>
      <span class="brand-name__sub">PROPERTY PARTNERS</span>
    </p>
  </section>
</body>
</html>
```